PPT template for boutique strategic planning, accounting and taxation firm

We are a boutique firm that provides strategic, accounting and tax advice to our clients. The work we are doing is increasingly strategic work and we are required to produce reports and presentations and our current templates are simply not sufficient.
As you can see from the examples attached, we have very limited skills in house re design! We have attached a PPT document and word document (that should be PPT) that we use regularly as examples of the content. Excel worksheets are regularly embedded into the presentation (in both blue and orange - see below re colours)
Not specific to one area but typically these clients are famous for their own brand and are creating value in their industry through creating their own brand and we want to produce documents of a similar standard.
A Powerpoint Document Slide Template
Cover page layout, back page, intermediate page heading, in colours and styles based on the logo, title styles, and an intermediate or chapter heading slide style. Many of our presentations contain slides with tables, diagrams, flowcharts and text, including simple lists of bullet points. As above, you will see in our style guide that we have three coloured logos – we would like one version in blue and one version in orange please. Again, the cover should be bold and draw attention but remain professional.
We are looking for something that works in both 4:3 and 16:9 (or two templates please)
We like a clear professional and simple look.
Deliverable: PowerPoint template file (.potx extension) for PowerPoint 2007 with at least a “cover” layout, a “title and content” layout, and a simplified slide layout, as well as “back cover”. Please embed any fonts used.
Target Market(s)
Many of our clients are retail clients or have strong brands of their own.
Industry/Entity Type
Accounting
Requirements
Must have
- Harrowby & Co logo on each page.
Must have a cover page (please be bold but professional)
A selection of "standard" slides - dot points, detailed written content, example diagrams, flow charts etc.
A back cover
Nice to have
- We would like to have a copy done in both the blue and orange versions attached. Happy for the winner to complete the other colour after the winner is selected.
Prefer Arial logo but open to suggestions. Must be easy to read and professional
Should not have
- Nothing cartoonish

```html
<!DOCTYPE html>
<html lang="en">
<head>
<meta charset="utf-8">
<title>Harrowby &amp; Co — Cover Slide</title>
<link href="https://fonts.googleapis.com/css2?family=Open+Sans:wght@400;600;700&display=swap" rel="stylesheet">
<style>
  :root {
    --brand-orange: #f47b20;
    --ink-dark: #4a4f56;
    --ink-body: #5a5e63;
    --paper: #ffffff;
    --paper-tint: #f3f3f3;
    --rule: #d9d9d9;
  }
  html, body {
    margin: 0;
    padding: 0;
    overflow: hidden;
    background: var(--paper);
  }
  .slide {
    position: relative;
    width: 1200px;
    height: 900px;
    overflow: hidden;
    background: var(--paper);
    font-family: "Open Sans", Arial, sans-serif;
  }
  .backdrop-texture {
    position: absolute;
    inset: 0;
    background:
      radial-gradient(ellipse 900px 700px at 95% 45%, rgba(255,255,255,1) 0%, rgba(255,255,255,0.85) 40%, rgba(255,255,255,0) 75%),
      linear-gradient(135deg, #e9e9e9 0%, #f4f4f4 45%, #fbfbfb 70%, #f6f6f6 100%);
  }
  .brand-tab {
    position: absolute;
    left: 0;
    top: 342px;
    width: 543px;
    height: 126px;
    background: var(--paper);
    border-radius: 0 63px 63px 0;
    box-shadow: 0 0 40px 14px rgba(244,123,32,0.22);
    display: flex;
    align-items: center;
    padding-left: 62px;
    box-sizing: border-box;
    gap: 18px;
  }
  .brand-dot {
    width: 100px;
    height: 100px;
    border-radius: 50%;
    background: var(--brand-orange);
    flex: none;
  }
  .brand-text {
    display: flex;
    flex-direction: column;
  }
  .brand-name {
    font-size: 50px;
    font-weight: 700;
    color: var(--ink-dark);
    line-height: 1;
    letter-spacing: -0.5px;
    white-space: nowrap;
  }
  .brand-tagline {
    margin-top: 8px;
    font-size: 13.5px;
    font-weight: 600;
    color: var(--ink-dark);
    white-space: nowrap;
  }
  .cover-heading {
    position: absolute;
    left: 633px;
    top: 344px;
    margin: 0;
    font-size: 45px;
    font-weight: 700;
    letter-spacing: 0.5px;
    color: var(--ink-dark);
    line-height: 1.2;
  }
  .cover-heading .accent { color: var(--brand-orange); }
  .heading-rule {
    position: absolute;
    left: 622px;
    top: 402px;
    width: 578px;
    height: 2px;
    background: linear-gradient(90deg, rgba(217,217,217,0) 0%, var(--rule) 8%, var(--rule) 100%);
  }
  .cover-summary {
    position: absolute;
    left: 633px;
    top: 414px;
    width: 545px;
    margin: 0;
    font-size: 22.5px;
    line-height: 39px;
    color: var(--ink-body);
  }
  .cover-summary strong { font-weight: 700; color: var(--ink-dark); }
  .footer-band {
    position: absolute;
    left: 0;
    bottom: 0;
    width: 100%;
    height: 45px;
    background: var(--brand-orange);
  }
  .page-number {
    position: absolute;
    right: 22px;
    top: 0;
    line-height: 45px;
    font-size: 19.5px;
    font-weight: 700;
    color: var(--paper);
  }
</style>
</head>
<body>
  <main class="slide">
    <div class="backdrop-texture" role="img" aria-label="Soft grey halftone dot texture sweeping across the background"></div>

    <div class="brand-tab">
      <div class="brand-dot"></div>
      <div class="brand-text">
        <span class="brand-name">Harrowby &amp; Co</span>
        <span class="brand-tagline">Accounting, Taxation &amp; Strategic Business Advisors</span>
      </div>
    </div>

    <h1 class="cover-heading"><span class="accent">PROJECT</span> TITLE HERE</h1>
    <div class="heading-rule"></div>
    <p class="cover-summary"><strong>Lorem ipsum dolor sit ipsum</strong> Lorem ipsum dolor sit ipsum Lorem ipsum Lorem ipsum dolor sit ipsum Lorem ipsum dolor sit ipsum Lorem ipsum.</p>

    <footer class="footer-band">
      <span class="page-number">Page : 01</span>
    </footer>
  </main>
</body>
</html>
```